Need a book cover design for a Lumora Book on Herbal Remedies

I need a book cover for my new ebook, here are the details:
Title: Meadow Cures
Sub-Heading: Buried Ancient Garden Tonics
Reclaiming the Wisdom of Roots for Everyday Wellness and Strength
Author: Nora Belcourt

```html
<!DOCTYPE html>
<html lang="en">
<head>
<meta charset="utf-8">
<title>Meadow Cures — Nora Belcourt</title>
<link rel="stylesheet" href="https://fonts.googleapis.com/css2?family=Jost:wght@400;600&display=swap">
<style>
  :root {
    --paper: #e4e0dc;
    --ink: #0b0b0b;
    --leaf: rgba(63,122,44,0.95);
    --leaf-soft: rgba(63,122,44,0.5);
    --leaf-deep: rgba(44,90,30,0.95);
    --bloom: rgba(168,135,201,0.55);
    --clear: rgba(228,224,220,0);
  }
  html, body {
    margin: 0;
    padding: 0;
    width: 752px;
    height: 1200px;
    overflow: hidden;
    background: var(--paper);
  }
  .cover {
    position: relative;
    width: 752px;
    height: 1200px;
    background: var(--paper);
    font-family: "Jost", sans-serif;
    color: var(--ink);
    overflow: hidden;
  }
  .herb-frame {
    position: absolute;
    inset: 0;
    background:
      radial-gradient(ellipse 480px 250px at 260px 0px, var(--leaf) 0%, var(--leaf-soft) 45%, var(--clear) 100%),
      radial-gradient(ellipse 300px 200px at 700px 40px, var(--leaf-soft) 0%, var(--clear) 100%),
      radial-gradient(ellipse 150px 300px at 752px 420px, var(--leaf) 0%, var(--leaf-soft) 45%, var(--clear) 100%),
      radial-gradient(ellipse 130px 120px at 640px 760px, var(--bloom) 0%, var(--clear) 100%),
      radial-gradient(ellipse 120px 180px at 0px 600px, var(--bloom) 0%, var(--clear) 100%),
      radial-gradient(ellipse 200px 260px at 0px 760px, var(--leaf) 0%, var(--leaf-soft) 45%, var(--clear) 100%),
      radial-gradient(ellipse 560px 330px at 376px 1200px, var(--leaf-deep) 0%, var(--leaf-soft) 50%, var(--clear) 100%),
      radial-gradient(ellipse 240px 360px at 752px 1060px, var(--leaf) 0%, var(--leaf-soft) 45%, var(--clear) 100%),
      radial-gradient(ellipse 240px 300px at 0px 1100px, var(--leaf) 0%, var(--leaf-soft) 45%, var(--clear) 100%);
  }
  .title {
    position: absolute;
    left: 0; right: 0;
    top: 300px;
    margin: 0;
    text-align: center;
    font-weight: 600;
    font-size: 88px;
    line-height: 101px;
    letter-spacing: 0.2em;
    text-indent: 0.2em;
    text-transform: uppercase;
  }
  .subtitle {
    position: absolute;
    left: 0; right: 0;
    top: 567px;
    margin: 0;
    text-align: center;
    font-weight: 400;
    font-size: 21px;
    line-height: 33px;
    letter-spacing: 0.02em;
    text-transform: uppercase;
  }
  .author {
    position: absolute;
    left: 0; right: 0;
    top: 783px;
    margin: 0;
    text-align: center;
    font-weight: 400;
    font-size: 50px;
    line-height: 50px;
    letter-spacing: 0.02em;
    text-transform: uppercase;
  }
</style>
</head>
<body>
  <main class="cover">
    <div class="herb-frame" role="img" aria-label="Photograph of fresh herbs — mint, rosemary, thyme, dill, parsley and flowering sage — framing the edges of the cover"></div>
    <h1 class="title">Meadow<br>Cures</h1>
    <p class="subtitle">Buried Ancient Garden Tonics:<br>Reclaiming the Wisdom of Roots<br>for Everyday Wellness and Strength</p>
    <p class="author">Nora Belcourt</p>
  </main>
</body>
</html>
```